The Orchard of Virtue Customized for my Business

Hi! I am interested in getting some design ideas to take this Orchard of Virtue and put a bit of branding of my business into it. Open to any and all designs, this is intended to put on a 20"x24" or 16"x20" canvas so I can have it in my office for team training purposes. I have included a picture of the wall this canvas will go on. Thank you!

```html
<!DOCTYPE html>
<html lang="en">
<head>
<meta charset="utf-8">
<title>The Orchard of Virtue</title>
<link rel="stylesheet" href="https://fonts.googleapis.com/css2?family=Outfit:wght@400;500;600;700;800&display=swap">
<style>
  :root {
    --page: #ffffff;
    --deep-blue: #283a8f;
    --mid-blue: #1c63b8;
    --bright-blue: #16a8e6;
    --frame-blue: #8ecdf1;
    --block: #ffffff;
    --stone: #636466;
    --ink: #111111;
    --logo-ink: #3d3d40;
  }
  * { box-sizing: border-box; margin: 0; padding: 0; }
  html, body {
    width: 1200px; height: 1026px; overflow: hidden;
    background: var(--page);
    font-family: "Outfit", sans-serif;
  }
  .stage {
    position: absolute; left: 0; top: 0;
    width: 2048px; height: 1751px;
    transform: scale(0.5859); transform-origin: 0 0;
  }
  .poster {
    position: absolute; left: 127px; top: 108px;
    width: 1813px; height: 1510px;
    background:
      linear-gradient(200deg, rgba(40,58,143,0.95) 0%, rgba(40,58,143,0) 45%),
      linear-gradient(20deg, var(--bright-blue) 0%, #2c86d3 35%, var(--mid-blue) 60%, var(--deep-blue) 100%);
    overflow: hidden;
  }
  .title {
    position: absolute; left: 195px; top: 165px;
    color: #fff; font-weight: 800; font-size: 94px; line-height: 118px;
    letter-spacing: -1px;
    text-shadow: 0 6px 14px rgba(0,0,0,0.35);
  }
  .brand-disc {
    position: absolute; left: 1405px; top: 153px;
    width: 500px; height: 500px; border-radius: 50%;
    background: #fff;
    display: flex; align-items: center; justify-content: center;
  }
  .brand-name {
    color: var(--logo-ink); font-weight: 700; font-size: 92px;
  }
  .pyramid-shape { position: absolute; left: 0; top: 0; }
  .block {
    position: absolute; background: var(--block);
    text-align: center; color: var(--ink);
    padding: 10px 6px 0;
  }
  .block h2 {
    font-weight: 600; font-size: 34px; line-height: 1.05;
    letter-spacing: -0.3px;
    margin-bottom: 8px;
  }
  .block h2.one-line { white-space: nowrap; font-size: 31px; letter-spacing: -0.6px; }
  .block h2.small { font-size: 25px; font-weight: 500; white-space: nowrap; }
  .block p {
    font-weight: 500; font-size: 20px; line-height: 1.5;
  }
  .block p.tight { line-height: 1.24; }
  .tag {
    position: absolute; color: #fff; text-align: center;
    transform: translate(-50%, -50%) rotate(var(--r));
    white-space: nowrap; line-height: 1.05;
  }
  .tag b { display: block; font-weight: 500; font-size: 23px; }
  .tag i { display: block; font-style: italic; font-size: 14px; }
  .tag.long b { font-size: 18px; }
  .tag.left { --r: -60deg; }
  .tag.right { --r: 60deg; }
</style>
</head>
<body>
<div class="stage">
  <div class="poster"></div>

  <h1 class="title">THE ORCHARD<br>OF VIRTUE</h1>

  <div class="brand-disc"><span class="brand-name">Millbrook</span></div>

  <svg class="pyramid-shape" width="2048" height="1751" viewBox="0 0 2048 1751" aria-hidden="true">
    <polygon points="1058,135 235,1560 1885,1560" fill="#8ecdf1" stroke="#a8dbf6" stroke-width="6"/>
    <g fill="#636466">
      <polygon points="1053,175 1053,378 935,378"/>
      <polygon points="1065,175 1065,378 1183,378"/>
      <polygon points="918,408 918,612 800,612"/>
      <polygon points="1200,408 1200,612 1318,612"/>
      <polygon points="783,642 783,845 665,845"/>
      <polygon points="1335,642 1335,845 1453,845"/>
      <polygon points="648,875 648,1078 530,1078"/>
      <polygon points="1470,875 1470,1078 1588,1078"/>
      <polygon points="515,1110 515,1310 397,1310"/>
      <polygon points="1605,1110 1605,1310 1722,1310"/>
      <polygon points="380,1345 380,1545 262,1545"/>
      <polygon points="1740,1345 1740,1545 1858,1545"/>
    </g>
  </svg>

  <div class="tag left" style="left:1015px;top:318px"><b>FAITH</b><i>(through<br>prayer)</i></div>
  <div class="tag right" style="left:1106px;top:312px"><b>PATIENCE</b><i>(good things<br>take time)</i></div>
  <div class="tag left" style="left:880px;top:553px"><b>FIGHT</b><i>(determined<br>effort)</i></div>
  <div class="tag right" style="left:1240px;top:548px"><b>INTEGRITY</b><i>(purity of<br>intention)</i></div>
  <div class="tag left long" style="left:750px;top:772px"><b>RESOURCEFULNESS</b><i>(proper<br>judgment)</i></div>
  <div class="tag right" style="left:1375px;top:775px"><b>RELIABILITY</b><i>(creates<br>respect)</i></div>
  <div class="tag left" style="left:610px;top:1005px"><b>ADAPTABILITY</b><i>(to any<br>situation)</i></div>
  <div class="tag right" style="left:1510px;top:1010px"><b>HONESTY</b><i>(in thought<br>and action)</i></div>
  <div class="tag left" style="left:474px;top:1240px"><b>AMBITION</b><i>(for noble<br>goals)</i></div>
  <div class="tag right" style="left:1645px;top:1243px"><b>SINCERITY</b><i>(keeps friends)</i></div>

  <!-- Row 1 -->
  <section class="block" style="left:935px;top:393px;width:250px;height:214px">
    <h2>COMPETITIVE GREATNESS</h2>
    <p class="tight">Be at our best when your best is needed. Enjoyment of a difficult challenge.</p>
  </section>

  <!-- Row 2 -->
  <section class="block" style="left:800px;top:627px;width:250px;height:213px;padding-top:30px">
    <h2>POISE</h2>
    <p class="tight" style="line-height:1.4">Just being yourself. Being at ease in any situation. Never fighting yourself.</p>
  </section>
  <section class="block" style="left:1070px;top:627px;width:250px;height:213px;padding-top:30px">
    <h2>CONFIDENCE</h2>
    <p style="line-height:1.9">Respect without fear. May come from being prepared and</p>
  </section>

  <!-- Row 3 -->
  <section class="block" style="left:665px;top:860px;width:250px;height:213px">
    <h2>CONDITION</h2>
    <p class="tight">Mental-Moral-Physical. Rest, exercise and diet must be considered. Moderation must be practiced. Dissipation must be eliminated.</p>
  </section>
  <section class="block" style="left:935px;top:860px;width:250px;height:213px">
    <h2>SKILL</h2>
    <p style="line-height:1.78">knowledge of and the ability to properly and quickly execute the fundamentals.</p>
  </section>
  <section class="block" style="left:1205px;top:860px;width:250px;height:213px">
    <h2>TEAM SPIRIT</h2>
    <p class="tight">A genuine consideration for others. An eagerness to sacrifice personal interests of glory for the welfare of all.</p>
  </section>

  <!-- Row 4 -->
  <section class="block" style="left:530px;top:1095px;width:250px;height:210px">
    <h2 class="one-line">SELF-CONTROL</h2>
    <p style="line-height:1.4">Practice self-discipline and keep emotions under control. Good judgment and common sense are essential.</p>
  </section>
  <section class="block" style="left:800px;top:1095px;width:250px;height:210px">
    <h2>ALERTNESS</h2>
    <p style="line-height:1.65">Be observing constantly. Stay open-minded. Be eager to learn and improve.</p>
  </section>
  <section class="block" style="left:1070px;top:1095px;width:250px;height:210px">
    <h2>INITIATIVE</h2>
    <p style="line-height:1.4">Cultivate the ability to make decisions and think alone. Do not be afraid of failure but, learn from it.</p>
  </section>
  <section class="block" style="left:1340px;top:1095px;width:250px;height:210px">
    <h2>INTENTNESS</h2>
    <p class="tight">Set a realistic goal. Concentrate on its achievement by resisting all temptations and being determined and persistent.</p>
  </section>

  <!-- Row 5 -->
  <section class="block" style="left:395px;top:1328px;width:250px;height:212px">
    <h2 class="small">INDUSTRIOUSNESS</h2>
    <p style="line-height:1.78">There is no substitute for work. Worthwhile results come from hard work and careful</p>
  </section>
  <section class="block" style="left:665px;top:1328px;width:250px;height:212px">
    <h2>FRIENDSHIP</h2>
    <p class="tight">Comes from mutual esteem, respect and devotion. Like marriage it must not be taken for granted but requires a joint effort.</p>
  </section>
  <section class="block" style="left:935px;top:1328px;width:250px;height:212px">
    <h2>LOYALTY</h2>
    <p style="line-height:1.78">To yourself and to all those depending upon you. Keep your self-respect.</p>
  </section>
  <section class="block" style="left:1205px;top:1328px;width:250px;height:212px">
    <h2 class="one-line">COOPERATION</h2>
    <p class="tight">With all levels of your co-workers. Listen if you want to be heard. Be interested in finding the best way, not in having your own way</p>
  </section>
  <section class="block" style="left:1475px;top:1328px;width:250px;height:212px">
    <h2>ENTHUSIASM</h2>
    <p style="line-height:1.52">Brushes off upon those with whom you come in contact. You must truly enjoy what you are doing.</p>
  </section>
</div>
</body>
</html>
```